Business Card For Kelmora Financial Consulting

Hi, I would like a business card designed. Bold, modern.
Please use the same design as the logo. I have also attached the website design to see the overall theme.
Wordmark Font
Color: Hex: #01AEF7

```html
<!DOCTYPE html>
<html lang="en">
<head>
<meta charset="utf-8">
<title>Kelmora Financial Consulting — Business Card</title>
<link href="https://fonts.googleapis.com/css2?family=Montserrat:wght@400;600;700&display=swap" rel="stylesheet">
<style>
  :root {
    --stage: #3b3b3b;
    --card: #17222d;
    --accent: #01aef7;
    --accent-soft: #2f9fe0;
    --ink: #ffffff;
    --ink-muted: #d7dde3;
  }
  * { box-sizing: border-box; margin: 0; padding: 0; }
  html, body {
    width: 1200px; height: 801px; overflow: hidden;
    background: var(--stage);
    font-family: "Montserrat", Arial, sans-serif;
  }
  .canvas {
    position: relative; width: 1200px; height: 801px;
    display: flex; align-items: center; justify-content: center; gap: 44px;
  }
  .card {
    position: relative; width: 525px; height: 300px;
    background: var(--card);
    border-bottom: 3px solid var(--accent);
    border-left: 2px solid var(--accent);
    box-shadow: 0 14px 30px rgba(0,0,0,0.35);
  }

  /* Contact side */
  .card-contact { display: flex; align-items: center; }
  .identity {
    width: 235px; padding-right: 22px; text-align: right;
  }
  .identity-name {
    color: var(--accent-soft); font-weight: 700; font-size: 21px;
    letter-spacing: 0.2px; text-transform: uppercase; line-height: 1.1;
  }
  .identity-role {
    color: var(--ink-muted); font-size: 14px; margin-top: 4px;
  }
  .divider {
    width: 2px; height: 84px; background: var(--accent-soft);
  }
  .details {
    list-style: none; padding-left: 20px;
    color: var(--ink); font-size: 13px; line-height: 1.42;
  }
  .details li { display: flex; align-items: center; gap: 6px; white-space: nowrap; }
  .details svg { width: 11px; height: 11px; flex: none; }
  .details .address { padding-left: 0; }

  /* Brand side */
  .card-brand { display: flex; align-items: center; justify-content: center; gap: 18px; }
  .brand-square {
    width: 58px; height: 58px; border: 5px solid var(--accent-soft); flex: none;
  }
  .brand-name {
    color: var(--ink); font-weight: 600; font-size: 30px;
    line-height: 1.12; letter-spacing: 1px; text-transform: uppercase;
  }
</style>
</head>
<body>
  <main class="canvas">
    <section class="card card-contact" aria-label="Contact side">
      <div class="identity">
        <p class="identity-name">Marlen Ostrava</p>
        <p class="identity-role">President</p>
      </div>
      <div class="divider"></div>
      <ul class="details">
        <li class="address">18420 Harbor Crest Dr</li>
        <li class="address">Seacliff CA 92701</li>
        <li>
          <svg viewBox="0 0 12 12" aria-hidden="true"><path fill="var(--accent)" d="M2.5 1l2 2.2-1 1.3a7 7 0 0 0 4 4l1.3-1 2.2 2-1.3 1.5C5.6 11 1 6.4 1 2.3z"/></svg>
          555-214-7730
        </li>
        <li>
          <svg viewBox="0 0 12 12" aria-hidden="true"><rect x="1" y="2.5" width="10" height="7" fill="var(--accent)"/><path d="M1 2.5l5 4 5-4" stroke="var(--card)" stroke-width="1" fill="none"/></svg>
          info@KelmoraConsulting.com
        </li>
        <li>
          <svg viewBox="0 0 12 12" aria-hidden="true"><circle cx="6" cy="6" r="5" fill="var(--accent)"/><path d="M1 6h10M6 1c-2.5 3-2.5 7 0 10M6 1c2.5 3 2.5 7 0 10" stroke="var(--card)" stroke-width="0.8" fill="none"/></svg>
          www.KelmoraConsulting.com
        </li>
      </ul>
    </section>

    <section class="card card-brand" aria-label="Brand side">
      <div class="brand-square"></div>
      <p class="brand-name">Kelmora<br>Financial Consulting</p>
    </section>
  </main>
</body>
</html>
```